Landscape Company Stationary
Biz cards, letterhead, envelopes, etc
Professional
Dean Morvik
P.O. Box 3852
Sparta, NJ 07634
foxridgemail@postbrim.com
Dont want address on biz cards, just letterhead and envelopes. Would like to incorporate the stripe and colors that are in our logo.
Logo with colors and fonts to use. Please incorporate the striping too and colors

```html
<!DOCTYPE html>
<html lang="en">
<head>
<meta charset="utf-8">
<title>Foxridge Landscapes – Business Cards</title>
<link href="https://fonts.googleapis.com/css2?family=Open+Sans:wght@400;600;700;800&display=swap" rel="stylesheet">
<style>
  :root {
    --sheet: #ececec;
    --card-border: #b9b9b9;
    --forest: #1f8a1c;
    --forest-deep: #16711a;
    --lime: #8fcf3c;
    --lime-soft: #b9e07a;
    --white: #ffffff;
    --ink: #333333;
  }
  * { box-sizing: border-box; margin: 0; padding: 0; }
  html, body { width: 1200px; height: 734px; overflow: hidden; }
  body {
    background: var(--sheet);
    font-family: "Open Sans", Arial, sans-serif;
    position: relative;
  }
  .card {
    position: absolute;
    width: 552px;
    height: 326px;
    border: 2px solid var(--card-border);
    overflow: hidden;
  }
  .card--front { left: 34px; top: 29px; background: var(--white); }
  .card--lime  { left: 614px; top: 29px; background: var(--lime); }
  .card--white { left: 34px; top: 377px; background: var(--white); }
  .card--forest{ left: 614px; top: 377px; background: var(--forest); }

  .card__header { position: absolute; left: 0; top: 0; width: 100%; height: 130px; }

  .contact {
    position: absolute;
    right: 24px;
    top: 16px;
    color: var(--white);
    font-size: 12.5px;
    line-height: 19px;
    text-align: right;
  }

  .wordmark {
    display: flex;
    align-items: center;
    gap: 10px;
    color: var(--forest);
    font-weight: 700;
    line-height: 1;
  }
  .wordmark__dot {
    width: 16px; height: 16px; border-radius: 50%;
    background: var(--lime);
    flex: none;
  }
  .wordmark__text { display: flex; flex-direction: column; }
  .wordmark__name { font-size: 52px; letter-spacing: -1px; }
  .wordmark__tag  { font-size: 17px; letter-spacing: 5px; margin-top: 4px; text-transform: uppercase; }

  .card--front .wordmark { position: absolute; left: 38px; top: 212px; }
  .card--front .wordmark__name { font-size: 44px; }
  .card--front .wordmark__tag  { font-size: 14px; letter-spacing: 4px; }

  .card--lime .wordmark,
  .card--white .wordmark,
  .card--forest .wordmark {
    position: absolute; left: 50%; top: 50%; transform: translate(-50%, -50%);
  }
  .card--lime .wordmark__dot { background: var(--white); }
  .card--forest .wordmark { color: var(--white); }

  .holder {
    position: absolute;
    right: 60px;
    top: 246px;
    text-align: right;
  }
  .holder__name { color: var(--forest); font-size: 21px; font-weight: 400; }
  .holder__role { color: var(--ink); font-size: 11px; margin-top: 4px; }
</style>
</head>
<body>

  <section class="card card--front">
    <svg class="card__header" viewBox="0 0 552 130" preserveAspectRatio="none" aria-hidden="true">
      <path d="M0,0 H552 V76 C440,74 330,96 230,108 C140,118 60,112 0,104 Z" fill="var(--forest)"/>
      <path d="M0,104 C60,112 140,118 230,108 C330,96 440,74 552,76 V86 C440,84 330,104 230,116 C140,126 60,120 0,112 Z" fill="var(--lime)"/>
    </svg>
    <div class="contact">
      <div>Phone: 973-555-0148</div>
      <div>Cell: 862-555-0172</div>
      <div>Email: foxridgemail@postbrim.com</div>
    </div>
    <div class="wordmark">
      <span class="wordmark__text">
        <span class="wordmark__name">Foxridge</span>
        <span class="wordmark__tag">Landscapes</span>
      </span>
      <span class="wordmark__dot"></span>
    </div>
    <div class="holder">
      <div class="holder__name">Dean Morvik</div>
      <div class="holder__role">Owner</div>
    </div>
  </section>

  <section class="card card--lime">
    <div class="wordmark">
      <span class="wordmark__text">
        <span class="wordmark__name">Foxridge</span>
        <span class="wordmark__tag">Landscapes</span>
      </span>
      <span class="wordmark__dot"></span>
    </div>
  </section>

  <section class="card card--white">
    <div class="wordmark">
      <span class="wordmark__text">
        <span class="wordmark__name">Foxridge</span>
        <span class="wordmark__tag">Landscapes</span>
      </span>
      <span class="wordmark__dot"></span>
    </div>
  </section>

  <section class="card card--forest">
    <div class="wordmark">
      <span class="wordmark__text">
        <span class="wordmark__name">Foxridge</span>
        <span class="wordmark__tag">Landscapes</span>
      </span>
      <span class="wordmark__dot"></span>
    </div>
  </section>

</body>
</html>
```